8 Page Publishing/Entertainment Website Design

We need a slick, polished, professional looking fully mobile responsive website designed for the publishing / entertainment industry. It will contain 8 pages, including the Home page. The site is to be designed in pure HTML and CSS only and to be compatible with any type of server we put it on. Pages are *not* to be part of any template system, like WordPress or others like it. Pure HTML and CSS standalone pages only. No WordPress or Joomla, etc. Website to use our logo's colors of red/white throughout its design. Uploaded files contain a word DOC that outlines more of our needs and we have included our logo file. Please read the specifications in the Word Document attached. We have also included a PDF file with the website specs as well.

Target Market(s)

Authors and Screenwriters

Coding

Coded - Design and coding required

Number of Pages Required

5+ page

Colors
ec1f27
ffffff
f04a50
f59195

Requirements
Must have
• The site is to be designed in pure HTML and CSS only and to be compatible with any type of server we put it on. Pages are *not* to be part of any template system, like WordPress or others like it. Pure HTML and CSS standalone pages only. No WordPress or Joomla, etc. Website to use our logo's colors of red/white throughout its design. Uploaded files contain a word DOC that outlines more of our needs and we have included our logo file. Please read the specifications in the Word Document attached. We have also included a PDF file with the website specs as well.
Should not have
• No Wordpress or other Template type pages. Pure HTML and CSS only. Some Javascript and JQuery is okay, upon approval.

```html
<!DOCTYPE html>
<html lang="en">
<head>
<meta charset="utf-8">
<title>Starward Quill Publishing</title>
<link href="https://fonts.googleapis.com/css2?family=Montserrat:wght@400;500;600;700&family=Playfair+Display:wght@700&display=swap" rel="stylesheet">
<style>
:root{
  --red:#ec1f27;
  --red-deep:#e0101d;
  --pink:#fbb6b8;
  --white:#ffffff;
  --ink:#222222;
  --grey-band:#e9e9e9;
  --grey-foot:#dcdcdc;
  --muted:#555555;
}
*{margin:0;padding:0;box-sizing:border-box}
html,body{width:1200px;height:3403px;overflow:hidden}
body{font-family:'Montserrat',sans-serif;color:var(--ink);background:var(--white);position:relative}
.abs{position:absolute}
.btn{position:absolute;background:var(--red);color:var(--white);border-radius:30px;font-weight:700;font-size:19px;display:flex;align-items:center;justify-content:center}

/* hero */
.hero{position:absolute;left:0;top:0;width:1200px;height:644px;background:radial-gradient(ellipse at 70% 45%,#5a4a40 0%,#2c2a2c 45%,#141518 100%)}
.hero-photo{position:absolute;inset:0;background:linear-gradient(180deg,rgba(0,0,0,.25),rgba(0,0,0,.45))}
.brand{position:absolute;left:86px;top:22px;display:flex;align-items:center;gap:12px}
.brand-dot{width:70px;height:70px;border-radius:50%;background:var(--red)}
.brand-name{color:var(--white);font-weight:700;font-size:20px;line-height:1.15;width:200px}
.nav{position:absolute;right:86px;top:38px;display:flex;gap:26px;font-size:14px;font-weight:500;color:var(--white)}
.hero-title{position:absolute;top:222px;width:1200px;text-align:center;color:var(--white);font-weight:700;font-size:50px}
.hero-text{position:absolute;top:292px;left:220px;width:760px;text-align:center;color:var(--white);font-size:21px;line-height:1.6}
.watch{position:absolute;top:382px;width:1200px;display:flex;justify-content:center;align-items:center;gap:14px;color:var(--white);font-weight:700;font-size:23px}

/* about */
.section-title{position:absolute;width:1200px;text-align:center;color:var(--red);font-weight:700;font-size:34px}
.feature-h{position:absolute;color:var(--red);font-weight:700;font-size:35px}
.feature-p{position:absolute;font-size:17px;line-height:28px;color:#333}
.img-fill{position:absolute}

/* news */
.news{position:absolute;left:0;top:1685px;width:1200px;height:486px;background:var(--pink)}
.card{position:absolute;top:120px;width:240px;height:238px;background:var(--white);padding:18px 16px}
.card-top{display:flex;justify-content:space-between;font-size:14px}
.card-top b{color:var(--red);font-weight:600}
.card-author{display:flex;gap:14px;margin-top:20px}
.avatar{width:42px;height:42px;background:#9a8677}
.card-name{color:var(--red);font-weight:700;font-size:16px}
.card-time{font-size:12px;color:#333}
.card-text{margin-top:14px;font-size:13px;line-height:19px;color:#333}
.timeline{position:absolute;left:86px;top:388px;width:1028px;height:6px;background:var(--white)}
.timeline-on{position:absolute;left:0;top:0;width:198px;height:6px;background:var(--red)}
.tl-label{position:absolute;top:408px;font-size:13px;font-weight:500;color:#333}

/* authors */
.authors-h{position:absolute;left:86px;top:2270px;color:var(--red);font-weight:700;font-size:36px}
.authors-p{position:absolute;left:86px;top:2348px;width:470px;font-size:15px;line-height:28px;color:#333}
.author-plate{position:absolute;left:617px;top:2558px;width:497px;height:116px;background:var(--red-deep);color:var(--white);text-align:center}

/* partners */
.partners{position:absolute;left:0;top:2751px;width:1200px;height:259px;background:var(--grey-band)}
.partner{position:absolute;top:90px;width:224px;text-align:center}
.partner-name{font-family:'Playfair Display',serif;font-size:30px;color:#111}
.partner-p{font-size:16px;line-height:26px;margin-top:12px;color:#222}
.divider{position:absolute;top:70px;width:1px;height:122px;background:#9a9a9a}
.arrow{position:absolute;top:108px;width:46px;height:46px;border-radius:50%;background:var(--red)}

/* footer */
.footer{position:absolute;left:0;top:3010px;width:1200px;height:393px;background:var(--grey-foot)}
.foot-col{position:absolute;top:50px}
.foot-col h4{font-size:20px;font-weight:600;margin-bottom:20px;color:#111}
.foot-col li{list-style:none;font-size:14px;line-height:25.6px;color:#222}
.follow li{display:flex;align-items:center;gap:10px;margin-bottom:8px}
.copy{position:absolute;top:344px;width:1200px;text-align:center;font-size:14px;font-weight:500}
</style>
</head>
<body>

<header class="hero">
  <div class="hero-photo" role="img" aria-label="Hands holding a tablet with books flying out, dim office background"></div>
  <div class="brand"><span class="brand-dot"></span><span class="brand-name">Starward Quill Publishing</span></div>
  <nav class="nav"><span>Home</span><span>About Sqp</span><span>Apply Now</span><span>Sqp Worlds</span><span>Sqp Authors</span><span>FAQ's</span><span>News</span><span>Contact Us</span></nav>
  <h1 class="hero-title">Starward Quill Publishing</h1>
  <p class="hero-text">Lorem ipsum dolor sit amet, consectetur adipiscing elit, sed do eiusmod tempor incididunt ut labore et dolore magna aliqua.</p>
  <div class="watch">Watch Video
    <svg width="38" height="38" viewBox="0 0 38 38"><circle cx="19" cy="19" r="16" fill="none" stroke="#fff" stroke-width="3"/><path d="M15 12 L26 19 L15 26 Z" fill="#fff"/></svg>
  </div>
  <div class="btn" style="left:483px;top:447px;width:214px;height:59px">Apply Now</div>
</header>

<h2 class="section-title" style="top:697px">ABOUT SQP</h2>

<div class="img-fill" style="left:86px;top:810px;width:513px;height:392px;background:linear-gradient(135deg,#1c2430,#3d5a7a 55%,#0d1a2b)" role="img" aria-label="Hand holding a stack of books dissolving into a tablet screen"></div>
<h3 class="feature-h" style="left:635px;top:845px">At vero eos et accusamus</h3>
<p class="feature-p" style="left:637px;top:910px;width:480px">Lorem ipsum dolor sit amet, consectetur adipiscing elit, sed do eiusmod tempor incididunt ut labore et dolore magna aliqua. Ut enim ad minim veniam, quis nostrud exercitation ullamco laboris nisi ut aliquip ex ea commodo consequat. Duis aute irure dolor in reprehenderit</p>
<div class="btn" style="left:637px;top:1086px;width:193px;height:60px">Read More</div>

<h3 class="feature-h" style="left:86px;top:1252px">At vero eos et accusamus</h3>
<p class="feature-p" style="left:86px;top:1316px;width:470px">Lorem ipsum dolor sit amet, consectetur adipiscing elit, sed do eiusmod tempor incididunt ut labore et dolore magna aliqua. Ut enim ad minim veniam, quis nostrud exercitation ullamco laboris nisi ut aliquip ex ea commodo consequat. Duis aute irure dolor in reprehenderit</p>
<div class="btn" style="left:86px;top:1492px;width:193px;height:61px">Read More</div>
<div class="img-fill" style="left:599px;top:1202px;width:512px;height:392px;background:linear-gradient(160deg,#dfe8ef,#8fb4cf 50%,#e8eef2)" role="img" aria-label="Open book pages curving over a stack of books with coloured tabs"></div>

<section class="news">
  <h2 class="section-title" style="top:66px">News</h2>
  <div class="card" style="left:86px"><div class="card-top"><span><b>Like</b> | Reply</span><svg width="20" height="18" viewBox="0 0 20 18"><path d="M1 8h4v10H1zM6 8l5-8c2 0 2 2 2 3l-1 4h6c1 0 2 1 2 2l-2 8H6z" fill="#ec1f27"/></svg></div><div class="card-author"><div class="avatar" role="img" aria-label="Author portrait"></div><div><div class="card-name">John Doe</div><div class="card-time">10 hours ago</div></div></div><p class="card-text">At vero eos et accusamus et iusto odio dignissimos ducimus qui blanditiis praesentium voluptatum deleniti atque corrupti quos dolores et</p></div>
  <div class="card" style="left:343px"><div class="card-top"><span><b>Like</b> | Reply</span><svg width="20" height="18" viewBox="0 0 20 18"><path d="M1 8h4v10H1zM6 8l5-8c2 0 2 2 2 3l-1 4h6c1 0 2 1 2 2l-2 8H6z" fill="#ec1f27"/></svg></div><div class="card-author"><div class="avatar" role="img" aria-label="Author portrait"></div><div><div class="card-name">John Doe</div><div class="card-time">10 hours ago</div></div></div><p class="card-text">At vero eos et accusamus et iusto odio dignissimos ducimus qui blanditiis praesentium voluptatum deleniti atque corrupti quos dolores et</p></div>
  <div class="card" style="left:608px"><div class="card-top"><span><b>Like</b> | Reply</span><svg width="20" height="18" viewBox="0 0 20 18"><path d="M1 8h4v10H1zM6 8l5-8c2 0 2 2 2 3l-1 4h6c1 0 2 1 2 2l-2 8H6z" fill="#ec1f27"/></svg></div><div class="card-author"><div class="avatar" role="img" aria-label="Author portrait"></div><div><div class="card-name">John Doe</div><div class="card-time">10 hours ago</div></div></div><p class="card-text">At vero eos et accusamus et iusto odio dignissimos ducimus qui blanditiis praesentium voluptatum deleniti atque corrupti quos dolores et</p></div>
  <div class="card" style="left:873px"><div class="card-top"><span><b>Like</b> | Reply</span><svg width="20" height="18" viewBox="0 0 20 18"><path d="M1 8h4v10H1zM6 8l5-8c2 0 2 2 2 3l-1 4h6c1 0 2 1 2 2l-2 8H6z" fill="#ec1f27"/></svg></div><div class="card-author"><div class="avatar" role="img" aria-label="Author portrait"></div><div><div class="card-name">John Doe</div><div class="card-time">10 hours ago</div></div></div><p class="card-text">At vero eos et accusamus et iusto odio dignissimos ducimus qui blanditiis praesentium voluptatum deleniti atque corrupti quos dolores et</p></div>
  <div class="timeline"><div class="timeline-on"></div><svg class="abs" style="left:92px;top:-10px" width="14" height="10" viewBox="0 0 14 10"><path d="M0 10L7 0L14 10Z" fill="#ec1f27"/></svg></div>
  <span class="tl-label" style="left:152px;color:var(--red)">10 hours ago</span>
  <span class="tl-label" style="left:352px">1 day ago</span>
  <span class="tl-label" style="left:498px">2 day ago</span>
  <span class="tl-label" style="left:641px">4 day ago</span>
  <span class="tl-label" style="left:798px">7 day ago</span>
  <span class="tl-label" style="left:992px">1 week ago</span>
</section>

<h2 class="authors-h">SQP Authors</h2>
<p class="authors-p">At vero eos et accusamus et iusto odio dignissimos ducimus qui blanditiis praesentium voluptatum deleniti atque corrupti quos dolores et quas molestias excepturi sint occaecati cupiditate non provident, similique sunt in culpa qui officia deserunt mollitia animi, id est laborum et dolorum fuga. Et harum quidem rerum facilis est et expedita distinctio.</p>
<div class="img-fill" style="left:617px;top:2254px;width:497px;height:304px;background:linear-gradient(120deg,#f2f2f0,#d9dde0 60%,#c7cbcf)" role="img" aria-label="Portrait of an author holding a pen, thinking, in a bright room"></div>
<div class="author-plate">
  <div style="margin-top:20px;font-weight:700;font-size:20px">Jayden</div>
  <div style="margin-top:6px;font-size:15px">Senior</div>
  <svg style="margin-top:8px" width="80" height="16" viewBox="0 0 80 16"><circle cx="8" cy="8" r="3" fill="#fff"/><circle cx="24" cy="8" r="3" fill="#fff"/><circle cx="40" cy="8" r="6" fill="none" stroke="#fff" stroke-width="2"/><circle cx="40" cy="8" r="3" fill="#fff"/><circle cx="56" cy="8" r="3" fill="#fff"/><circle cx="72" cy="8" r="3" fill="#fff"/></svg>
</div>

<section class="partners">
  <svg class="arrow" style="left:86px" viewBox="0 0 46 46"><circle cx="23" cy="23" r="23" fill="#ec1f27"/><path d="M26 14L17 23L26 32" fill="none" stroke="#fff" stroke-width="3"/></svg>
  <div class="partner" style="left:154px"><div class="partner-name">Ledgerline</div><p class="partner-p">At vero eos et accusamus<br>et iusto odio</p></div>
  <div class="divider" style="left:374px"></div>
  <div class="partner" style="left:379px"><div class="partner-name">Venturist</div><p class="partner-p">At vero eos et accusamus<br>et iusto odio</p></div>
  <div class="divider" style="left:597px"></div>
  <div class="partner" style="left:601px"><div class="partner-name" style="font-family:'Montserrat',sans-serif;font-weight:600;font-size:26px">tradehub.net</div><p class="partner-p">At vero eos et accusamus<br>et iusto odio</p></div>
  <div class="divider" style="left:821px"></div>
  <div class="partner" style="left:825px"><div class="partner-name">Inkfounder</div><p class="partner-p">At vero eos et accusamus<br>et iusto odio</p></div>
  <svg class="arrow" style="left:1066px" viewBox="0 0 46 46"><circle cx="23" cy="23" r="23" fill="#ec1f27"/><path d="M20 14L29 23L20 32" fill="none" stroke="#fff" stroke-width="3"/></svg>
</section>

<footer class="footer">
  <div class="abs" style="left:86px;top:96px;width:190px;display:flex;flex-direction:column;align-items:center;gap:12px">
    <span style="width:90px;height:90px;border-radius:50%;background:var(--red)"></span>
    <span style="color:var(--red);font-weight:700;font-size:18px;text-align:center;line-height:1.25">Starward Quill Publishing</span>
  </div>
  <div class="foot-col" style="left:431px"><h4>Quick Links</h4><ul><li>Home</li><li>About Sqp</li><li>Apply Now</li><li>Sqp Worlds</li><li>Sqp Authors</li><li>FAQ's</li><li>News</li><li>Contact Us</li></ul></div>
  <div class="foot-col" style="left:687px"><h4>Discover</h4><ul><li>Support</li><li>Tutorials</li><li>Privacy Policy</li><li>Terms and Conditions</li></ul></div>
  <div class="foot-col follow" style="left:941px"><h4>Follow</h4><ul>
    <li><svg width="16" height="16"><circle cx="8" cy="8" r="7" fill="#222"/></svg>|&nbsp; Chirpline</li>
    <li><svg width="16" height="16"><rect x="1" y="1" width="14" height="14" fill="#222"/></svg>|&nbsp; Journal</li>
  </ul></div>
  <p class="copy">© 2018 Copyrights | All Rights Reserved.</p>
</footer>

</body>
</html>
```